Psychiatrist/ Psychotherapist needs a letterhead design

I am a Psychiatrist working in private practice. I work as a psychotherapist and treat patients with depression, anxiety, post traumatic stress and relationship problems. I need a letterhead which is elegant and professional. I would like to see designs using colours such as blues and greys.
I would like the information on the letterhead split between the top and bottom of the page to give it a look of balance.
I want it to look elegant, feminine and upmarket. I don't want it to look too corporate but to show some flair and to be a bit artistic.

Target Market(s)

Other doctors, specialists and agencies who have referred patients to me.

Industry/Entity Type

Work

Font styles to use
Script

Requirements
Must have
• My name and my profession psychiatrist need to be highlighted and prominent. It needs to be professional looking and elegant without being old fashioned or too conservative.
Nice to have
• Balance between the top and bottom of the page.
Should not have
• I don't want fonts which are old and too traditional.

```html
<!DOCTYPE html>
<html lang="en">
<head>
<meta charset="utf-8">
<title>Dr Miriam Ashcombe – Letterhead</title>
<link rel="stylesheet" href="https://fonts.googleapis.com/css2?family=Arimo:wght@400;700&display=swap">
<style>
  :root {
    --paper: #ececec;
    --brand-blue: #0a86cf;
    --deep-blue: #0870b3;
    --ink: #111111;
    --on-blue: #ffffff;
  }
  html, body {
    margin: 0;
    padding: 0;
    overflow: hidden;
    background: var(--paper);
  }
  .letterhead {
    position: relative;
    width: 982px;
    height: 1200px;
    background: var(--paper);
    overflow: hidden;
    font-family: "Arimo", Arial, sans-serif;
  }
  .wave-art {
    position: absolute;
    inset: 0;
    width: 100%;
    height: 100%;
  }
  .sender {
    position: absolute;
    left: 84px;
    top: 114px;
    color: var(--ink);
  }
  .sender__name {
    margin: 0 0 4px;
    font-size: 22px;
    font-weight: 700;
    color: var(--brand-blue);
    letter-spacing: 0.2px;
  }
  .sender__title {
    margin: 0 0 3px;
    font-size: 14px;
    font-weight: 700;
  }
  .sender__address {
    margin: 0;
    font-size: 14px;
    font-style: normal;
  }
  .contact {
    position: absolute;
    left: 82px;
    top: 1042px;
    color: var(--on-blue);
    font-size: 17px;
    line-height: 21px;
  }
  .contact__row { display: flex; }
  .contact__label { width: 62px; }
</style>
</head>
<body>
<main class="letterhead">
  <svg class="wave-art" viewBox="0 0 517 667" preserveAspectRatio="none" aria-hidden="true">
    <!-- top right corner swoosh -->
    <path d="M352,0 C386,6 388,38 377,58 C368,76 388,82 412,76 C452,68 500,70 517,96 L517,0 Z" fill="var(--brand-blue)"/>
    <path d="M362,0 C392,8 394,40 384,60 C378,72 395,76 414,72 C450,64 498,64 517,86" fill="none" stroke="var(--paper)" stroke-width="2.5"/>
    <!-- bottom left swoosh -->
    <path d="M0,488 C40,540 120,552 170,557 C212,562 218,588 222,610 C228,642 262,660 300,667 L0,667 Z" fill="var(--brand-blue)"/>
    <path d="M0,494 C50,536 130,542 180,548 C215,553 222,585 226,606 C232,640 268,658 310,667" fill="none" stroke="var(--paper)" stroke-width="4"/>
    <path d="M0,500 C36,528 110,538 160,545 C190,549 200,562 205,580" fill="none" stroke="var(--deep-blue)" stroke-width="3" opacity="0.6"/>
  </svg>

  <header class="sender">
    <h1 class="sender__name">Dr Miriam Ashcombe</h1>
    <p class="sender__title">B.Med, FRANZCP Psychiatrist</p>
    <address class="sender__address">14 Fenwick Lane, Norwood, SA 5067</address>
  </header>

  <footer class="contact">
    <div class="contact__row"><span class="contact__label">Tel</span><span>: (08) 8140 5276</span></div>
    <div class="contact__row"><span class="contact__label">Fax</span><span>: (08) 8140 5290</span></div>
    <div class="contact__row"><span class="contact__label">Mob</span><span>: 0412705863</span></div>
    <div class="contact__row"><span>mashcombe@mailhub.net.au</span></div>
  </footer>
</main>
</body>
</html>
```